Redesign Two Website Pages (Homepage & Features) — Modern, Responsive, and Visually Engaging

We’re looking to redesign two pages of our website:

Homepage: https://velmorank.com
Features Page: https://velmorank.com/features

We already have a preliminary design in Figma for the homepage, but it currently feels too plain. Please don’t use this Figma file provided. It was only shared for facilitate using the current website content and not as a source for inspiration. Use your creativity to bring something fresh and less dull as the current design.

We want to enhance it with visually engaging elements, such as illustrations, graphics, or images that align with the content and the application’s purpose, making the design more dynamic and marketing-oriented.

Requirements:
- Create modern, visually appealing designs for both pages.
- Include relevant visuals (images or vector graphics) that complement the content and improve user engagement.
- Ensure full responsiveness across all major viewports: desktop, tablet, and mobile.
- Deliver the final design in Figma format.
- You can choose any colour palette that best fits the concept, but please retain the existing content from the live website.
- We’re looking for a clean, modern, and commercially appealing design that effectively communicates the value of our product.

Target Market(s)

B2B

Number of Pages Required

2 page

Font styles to use
Sans Serif

Requirements
Must have
• Images and graphics to make the design and product more attractive.

```html
<!DOCTYPE html>
<html lang="en">
<head>
<meta charset="utf-8">
<title>VELMORANK — Homepage &amp; Features</title>
<link href="https://fonts.googleapis.com/css2?family=Inter:wght@400;500;600;700;800&display=swap" rel="stylesheet">
<style>
:root{
  --backdrop:#b5b5b5;
  --page:#030817;
  --card:#070e22;
  --card-border:#141c36;
  --line:#0f1730;
  --text:#ffffff;
  --muted:#c3c9d8;
  --dim:#7e879c;
  --blue:#1e8bf0;
  --accent:#4fb4f6;
  --ghost:#1a2236;
}
*{box-sizing:border-box;margin:0;padding:0}
html,body{width:1200px;height:861px;overflow:hidden;background:var(--backdrop)}
body{font-family:'Inter',sans-serif;color:var(--text)}
.stage{position:absolute;left:0;top:0;width:2268px;height:1627px;transform:scale(0.529101);transform-origin:0 0;background:var(--backdrop)}
.page{position:absolute;width:1024px;background:var(--page);box-shadow:0 10px 30px rgba(0,0,0,.25);overflow:hidden}
.page--home{left:80px;top:80px;height:1467px}
.page--features{left:1164px;top:80px;height:1219px}
.abs{position:absolute}

/* nav */
.nav{position:absolute;left:0;top:0;width:100%;height:34px;border-bottom:1px solid var(--line)}
.brand{position:absolute;left:181px;top:7px;display:flex;align-items:center;gap:6px}
.brand-mark{width:14px;height:14px;border-radius:50%;background:var(--blue)}
.brand-name{font-size:10px;font-weight:500;line-height:10px}
.brand-tag{font-size:6px;color:var(--muted);line-height:8px}
.nav-links{position:absolute;top:8px;display:flex;gap:4px;font-size:7.5px;font-weight:500}
.nav-links span{padding:5px 6px;border-radius:4px}
.nav-links .active{background:var(--ghost)}
.nav-signin{position:absolute;left:738px;top:13px;font-size:7.5px}
.nav-cta{position:absolute;left:773px;top:8px;width:67px;height:18px;border-radius:4px;background:var(--blue);font-size:7.5px;font-weight:600;display:flex;align-items:center;justify-content:center}

.btn{position:absolute;height:25px;border-radius:5px;font-size:8.5px;font-weight:600;display:flex;align-items:center;justify-content:center}
.btn--primary{background:var(--blue)}
.btn--ghost{background:var(--ghost)}
.divider{position:absolute;left:0;width:100%;height:1px;background:var(--line)}

.card{position:absolute;background:var(--card);border:1px solid var(--card-border);border-radius:6px;padding:13px 13px}
.card h4{font-size:8.5px;font-weight:600;margin-bottom:5px}
.card p{font-size:6.5px;line-height:10px;color:var(--muted)}
.card--lg h4{font-size:9.5px;margin-bottom:8px}
.card--lg p{font-size:7px;line-height:10.5px}

/* hero */
.badge{position:absolute;left:183px;top:86px;height:13px;padding:0 6px;border-radius:7px;background:var(--card);border:1px solid var(--card-border);font-size:5.5px;display:flex;align-items:center;gap:4px}
.badge i{width:4px;height:4px;border-radius:50%;background:var(--accent)}
.hero-title{position:absolute;left:183px;top:106px;font-size:24px;font-weight:800;line-height:25px;letter-spacing:-.4px}
.hero-title em{font-style:normal;color:var(--accent)}
.hero-copy{position:absolute;left:183px;top:169px;width:318px;font-size:8.5px;line-height:15px;color:#e6e9f0}
.stat{position:absolute;top:273px;width:60px;text-align:center}
.stat b{display:block;font-size:14px;font-weight:700;line-height:16px}
.stat span{font-size:5px;color:var(--dim)}
.art{position:absolute;border-radius:6px}
.art--hero{left:520px;top:55px;width:322px;height:272px;background:linear-gradient(135deg,#e8f3fc 0%,#b6dcf8 55%,#8cc6f3 100%)}
.art--evidence{left:182px;top:741px;width:321px;height:321px;background:linear-gradient(160deg,#f3f5fb 0%,#dfe5f3 70%,#cfd8ee 100%)}

.trusted{position:absolute;left:183px;top:387px;font-size:10px;color:#dfe3ec}
.logo-slot{position:absolute;top:414px;width:99px;height:21px;border-radius:3px;background:#0a1226}

.sec-title{position:absolute;font-size:16px;font-weight:700;line-height:19px}
.sec-copy{position:absolute;font-size:8px;line-height:12.5px;color:#dfe3ec}
.link{position:absolute;font-size:8px;color:var(--accent)}

.list{list-style:none;font-size:8px;line-height:17px;color:#dfe3ec}

.cta-title{position:absolute;left:0;width:100%;text-align:center;font-size:16px;font-weight:700}
.cta-copy{position:absolute;left:0;width:100%;text-align:center;font-size:8px;color:#dfe3ec}

/* footer */
.f-col{position:absolute;font-size:7px;line-height:15px;color:#dfe3ec}
.f-col h5{font-size:7px;font-weight:700;color:var(--text);margin-bottom:2px}
.f-about{width:152px;line-height:10.5px}
.f-input{position:absolute;width:98px;height:19px;border:1px solid var(--card-border);border-radius:4px;background:var(--card);font-size:6.5px;color:var(--dim);padding-left:7px;display:flex;align-items:center}
.f-sub{position:absolute;width:53px;height:19px;border-radius:4px;background:var(--blue);font-size:7px;font-weight:600;display:flex;align-items:center;justify-content:center}
.copyright{position:absolute;left:0;width:100%;text-align:center;font-size:5.5px;color:var(--muted)}

/* features page */
.page-title{position:absolute;left:183px;top:76px;font-size:27px;font-weight:800;letter-spacing:-.4px}
.why{position:absolute;left:632px;top:198px;width:209px;height:212px;background:var(--card);border:1px solid var(--card-border);border-radius:6px;padding:14px 13px}
.why h4{font-size:8.5px;font-weight:600;margin-bottom:5px}
.why li{font-size:6.5px;line-height:15px;color:#dfe3ec;list-style:none}
.why .why-btn{margin-top:8px;width:64px;height:19px;border-radius:4px;background:var(--blue);font-size:7.5px;font-weight:600;display:flex;align-items:center;justify-content:center}
.sub-title{position:absolute;left:183px;font-size:12px;font-weight:700}
.plans{position:absolute;left:183px;top:657px;width:658px;border:1px solid var(--card-border);border-radius:6px;border-collapse:separate;border-spacing:0;overflow:hidden;font-size:6.5px}
.plans th,.plans td{height:28px;text-align:left;padding-left:9px;border-bottom:1px solid var(--line)}
.plans th{background:var(--card);font-weight:600}
.plans tr:last-child td{border-bottom:none}
.note{position:absolute;left:183px;top:812px;font-size:6px;color:var(--muted)}
</style>
</head>
<body>
<div class="stage">

  <!-- Homepage -->
  <section class="page page--home" aria-label="Homepage">
    <header class="nav">
      <div class="brand"><span class="brand-mark"></span><div><div class="brand-name">VELMORANK</div><div class="brand-tag">Guiding every audit with clarity</div></div></div>
      <nav class="nav-links" style="left:453px"><span class="active">Home</span><span>Features</span><span>Pricing</span><span>Docs</span></nav>
      <span class="nav-signin">Sign in</span>
      <span class="nav-cta">Start free trial</span>
    </header>

    <span class="badge"><i></i>New: AI-assisted risk scoring</span>
    <h1 class="hero-title">Guiding every audit <em>with</em><br><em>clarity</em></h1>
    <p class="hero-copy">Plan, execute, and report audits faster. VELMORANK centralizes evidence, automates workpapers, and keeps your team aligned from kickoff to close.</p>
    <span class="btn btn--primary" style="left:183px;top:229px;width:89px">Explore features</span>
    <span class="btn btn--ghost" style="left:279px;top:229px;width:74px">Book a demo</span>
    <div class="stat" style="left:202px"><b>40%</b><span>Faster fieldwork</span></div>
    <div class="stat" style="left:312px"><b>99.9%</b><span>Uptime</span></div>
    <div class="stat" style="left:422px"><b>GDPR</b><span>Ready</span></div>
    <div class="art art--hero" role="img" aria-label="Illustration of an auditor seated at a large tilted dashboard with charts and data cards"></div>

    <div class="divider" style="top:351px"></div>
    <p class="trusted">Trusted by internal audit teams across industries</p>
    <span class="logo-slot" style="left:183px"></span>
    <span class="logo-slot" style="left:295px"></span>
    <span class="logo-slot" style="left:406px"></span>
    <span class="logo-slot" style="left:518px"></span>
    <span class="logo-slot" style="left:630px"></span>
    <span class="logo-slot" style="left:741px"></span>

    <h2 class="sec-title" style="left:183px;top:512px;width:200px">Everything you need to run audits end-to-end</h2>
    <p class="sec-copy" style="left:183px;top:557px;width:210px">From planning and risk assessment to issue tracking and reporting—VELMORANK keeps your evidence, workpapers, and approvals in one place.</p>
    <span class="link" style="left:183px;top:609px">See all features →</span>
    <div class="card card--lg" style="left:407px;top:512px;width:211px;height:66px"><h4>Planning &amp; Scoping</h4><p>Define objectives, risks, and controls. Auto-build work programs from templates.</p></div>
    <div class="card card--lg" style="left:630px;top:512px;width:211px;height:66px"><h4>Fieldwork &amp; Evidence</h4><p>Assign procedures, capture evidence, and keep approvals moving.</p></div>
    <div class="card card--lg" style="left:407px;top:591px;width:211px;height:66px"><h4>Issues &amp; Actions</h4><p>Log findings, track owners and due dates, and monitor remediation.</p></div>
    <div class="card card--lg" style="left:630px;top:591px;width:211px;height:66px"><h4>Reporting</h4><p>Generate consistent, audit-ready reports in one click.</p></div>

    <div class="divider" style="top:700px"></div>
    <div class="art art--evidence" role="img" aria-label="Illustration of a person arranging evidence checklists on a large tablet screen"></div>
    <h3 class="sec-title" style="left:522px;top:849px;font-size:12.5px">Audit evidence, simplified</h3>
    <p class="sec-copy" style="left:522px;top:873px;width:310px">Request, collect, and organize evidence with smart checklists and version history. Link procedures to risks and controls for clear traceability.</p>
    <ul class="list abs" style="left:522px;top:906px">
      <li>• Smart templates for recurring audits</li>
      <li>• Inline comments &amp; reviewer sign-offs</li>
      <li>• Attachments, tags, and audit trails</li>
    </ul>

    <h2 class="cta-title" style="top:1146px">Ready to move faster?</h2>
    <p class="cta-copy" style="top:1173px">Start your 14-day free trial or book a guided walkthrough with our team.</p>
    <span class="btn btn--primary" style="left:432px;top:1197px;width:78px">Start free trial</span>
    <span class="btn btn--ghost" style="left:517px;top:1197px;width:74px">Book a demo</span>

    <div class="divider" style="top:1317px"></div>
    <div class="f-col f-about" style="left:183px;top:1338px"><h5>VELMORANK</h5>Guiding every audit with clarity. Streamline planning, evidence, and reporting in one platform.</div>
    <div class="f-col" style="left:352px;top:1338px"><h5>Product</h5>Features<br>Pricing<br>Security<br>Status</div>
    <div class="f-col" style="left:520px;top:1338px"><h5>Company</h5>About<br>Blog<br>Contact<br>Careers</div>
    <div class="f-col" style="left:689px;top:1338px"><h5>Get the latest</h5></div>
    <span class="f-input" style="left:689px;top:1356px">Email address</span>
    <span class="f-sub" style="left:792px;top:1356px">Subscribe</span>
    <p class="copyright" style="top:1446px">© 2025 VELMORANK. All rights reserved.</p>
  </section>

  <!-- Features page -->
  <section class="page page--features" aria-label="Features page">
    <header class="nav">
      <div class="brand"><span class="brand-mark"></span><div><div class="brand-name">VELMORANK</div><div class="brand-tag">Guiding every audit with clarity</div></div></div>
      <nav class="nav-links" style="left:459px"><span>Home</span><span class="active">Features</span><span>Pricing</span><span>Docs</span></nav>
      <span class="nav-signin">Sign in</span>
      <span class="nav-cta">Start free trial</span>
    </header>

    <h1 class="page-title">Features</h1>
    <p class="sec-copy" style="left:183px;top:110px;width:380px;font-size:8.5px;line-height:15px">A unified platform for planning, executing, and reporting audits. Built for clarity, collaboration, and consistent outcomes.</p>

    <div class="card" style="left:183px;top:198px;width:211px;height:63px"><h4>Templates &amp; Programs</h4><p>Kick off with best-practice programs you can tailor to each audit.</p></div>
    <div class="card" style="left:406px;top:198px;width:211px;height:63px"><h4>Assignments &amp; Workflow</h4><p>Assign tasks, set due dates, and keep reviewers in the loop.</p></div>
    <div class="card" style="left:183px;top:273px;width:211px;height:63px"><h4>Workpapers</h4><p>Attach evidence, add annotations, and maintain clear audit trails.</p></div>
    <div class="card" style="left:406px;top:273px;width:211px;height:63px"><h4>Issue Tracking</h4><p>Log findings, owners, due dates, and monitor remediation.</p></div>
    <div class="card" style="left:183px;top:347px;width:211px;height:63px"><h4>Reporting</h4><p>Generate consistent reports and export to PDF/Excel.</p></div>
    <div class="card" style="left:406px;top:347px;width:211px;height:63px"><h4>Security</h4><p>Role-based access, SSO (SAML/OIDC), and encryption at rest.</p></div>
    <aside class="why">
      <h4>Why teams choose VELMORANK</h4>
      <ul>
        <li>• Faster cycles with reusable templates</li>
        <li>• Evidence traceability &amp; audit trail</li>
        <li>• Reviewer sign-offs and approvals</li>
        <li>• Secure, role-based access</li>
        <li>• Export to PDF/Excel</li>
      </ul>
      <div class="why-btn">Get a demo</div>
    </aside>

    <div class="divider" style="top:428px"></div>
    <h2 class="sub-title" style="top:463px">Deep dives</h2>
    <div class="card" style="left:183px;top:495px;width:211px;height:65px"><h4>Risk &amp; Control Matrix</h4><p>Link procedures to risks and controls, visualize coverage, and surface gaps automatically.</p></div>
    <div class="card" style="left:406px;top:495px;width:211px;height:65px"><h4>Evidence Requests</h4><p>Send secure requests, track submissions and versions, and keep everything in one place.</p></div>
    <div class="card" style="left:629px;top:495px;width:212px;height:65px"><h4>AI Assistance</h4><p>Draft procedures, summarize findings, and generate consistent reports with AI support.</p></div>

    <h2 class="sub-title" style="top:629px">Compare plans</h2>
    <table class="plans">
      <colgroup><col style="width:175px"><col style="width:106px"><col style="width:141px"><col></colgroup>
      <tr><th>Feature</th><th>Starter</th><th>Growth</th><th>Enterprise</th></tr>
      <tr><td>Users included</td><td>5</td><td>20</td><td>Unlimited</td></tr>
      <tr><td>Templates</td><td>Basic</td><td>Advanced</td><td>Custom + SSO</td></tr>
      <tr><td>AI assistance</td><td>–</td><td>Summaries</td><td>Summaries + Drafting</td></tr>
      <tr><td>Support</td><td>Email</td><td>Priority</td><td>Dedicated CSM</td></tr>
    </table>
    <p class="note">* Demo table for contest file. Replace with final plan details.</p>

    <h2 class="cta-title" style="top:898px">Design looks good? Let’s make it yours.</h2>
    <p class="cta-copy" style="top:925px">We’ll adapt the color palette and visuals to your brand and migrate your existing content.</p>
    <span class="btn btn--primary" style="left:471px;top:950px;width:82px">Start free trial</span>

    <div class="divider" style="top:1069px"></div>
    <div class="f-col f-about" style="left:183px;top:1090px"><h5>VELMORANK</h5>Guiding every audit with clarity. Streamline planning, evidence, and reporting in one platform.</div>
    <div class="f-col" style="left:352px;top:1090px"><h5>Product</h5>Features<br>Pricing<br>Security<br>Status</div>
    <div class="f-col" style="left:520px;top:1090px"><h5>Company</h5>About<br>Blog<br>Contact<br>Careers</div>
    <div class="f-col" style="left:689px;top:1090px"><h5>Get the latest</h5></div>
    <span class="f-input" style="left:689px;top:1108px">Email address</span>
    <span class="f-sub" style="left:792px;top:1108px">Subscribe</span>
    <p class="copyright" style="top:1198px">© 2025 VELMORANK. All rights reserved.</p>
  </section>

</div>
</body>
</html>
```